Plakat-Design (LED-Wand) für Heizung-/Sanitär- und Klimatechnik
Zielgruppe
Heizung Sanitär und Klimatechnik
Aufgabenstellung
Wir möchten Regional in unserer Stadt auf einer LED Wand werben.
Unser Logo soll vertreten sein und unsere Telefonnummer. Da es auf den Winter zu geht wollen wir darauf aufmerksam machen, dass wir z.B. bei einem Heizungsausfall/Reparatur ein Ansprechpartner sind. z.B.: Heizung kalt? Wir machen es Ihnen warm ums Herz!
Gerne auch eigene Ideen.
Stockbilder können gerne mit eingebracht werden. Ist aber kein Muss.
Die Anzeige auf der LED Wand beträgt 6 Sekunden. Diese befindet sich auf einer Straßenverkehrskreuzung. Es soll also nicht überladen sein. Das Logo (Symbol und Schriftzug, kann wenn erforderlich auch nebeneinander gesetzt werden)
Anforderung der LED Wand: 800x600px 72dpi als JPG.

```html
<!DOCTYPE html>
<html lang="de">
<head>
<meta charset="utf-8">
<title>Heizung kalt? – Wärmehaus Tellbrink</title>
<link rel="stylesheet" href="https://fonts.googleapis.com/css2?family=Bangers&family=Open+Sans:wght@400;600&display=swap">
<style>
  :root {
    --page-bg: #e4e6ea;
    --ice-blue-dark: #1f3a93;
    --ice-blue: #1b7fd0;
    --warm-orange: #f06a12;
    --warm-yellow: #f7c21b;
    --phone-blue: #1561b5;
    --wall-light: #f4f5f7;
    --wall-mid: #d9dcdf;
    --photo-dark: #2a2d34;
    --denim: #3a5a93;
    --logo-blue: #1d6fc0;
    --band-white: rgba(255,255,255,0.92);
  }
  * { box-sizing: border-box; margin: 0; padding: 0; }
  html, body {
    width: 1200px; height: 758px; overflow: hidden;
    background: var(--page-bg);
  }
  .led-poster {
    position: absolute;
    left: 140px; top: 34px;
    width: 920px; height: 690px;
    overflow: hidden;
    background: var(--wall-light);
  }
  .poster-photo {
    position: absolute; inset: 0;
    background:
      linear-gradient(180deg, transparent 72%, rgba(200,200,205,0.55) 100%),
      linear-gradient(90deg, var(--photo-dark) 0%, #4b4f58 20%, var(--denim) 34%, var(--wall-mid) 46%, var(--wall-light) 70%, #e6e7ea 100%);
  }
  .headline-block {
    position: absolute;
    left: 405px; top: 110px;
    width: 490px;
  }
  .headline-cold {
    font-family: "Bangers", system-ui, sans-serif;
    font-size: 82px; line-height: 1;
    letter-spacing: 2px;
    background: linear-gradient(90deg, var(--ice-blue-dark), var(--ice-blue));
    -webkit-background-clip: text; background-clip: text;
    color: transparent;
    white-space: nowrap;
  }
  .headline-lead {
    font-family: "Open Sans", sans-serif;
    font-size: 24px; font-weight: 400;
    color: var(--ice-blue-dark);
    margin: 4px 0 0 -20px;
  }
  .headline-warm {
    font-family: "Bangers", system-ui, sans-serif;
    font-size: 74px; line-height: 1;
    letter-spacing: 2px;
    background: linear-gradient(90deg, var(--warm-orange), var(--warm-yellow) 70%, var(--warm-orange));
    -webkit-background-clip: text; background-clip: text;
    color: transparent;
    margin-top: 2px;
    white-space: nowrap;
  }
  .phone-number {
    font-family: "Bangers", system-ui, sans-serif;
    font-size: 56px; line-height: 1;
    letter-spacing: 1px;
    color: var(--phone-blue);
    margin-top: 16px;
    white-space: nowrap;
  }
  .brand-band {
    position: absolute;
    left: 0; bottom: 0;
    width: 470px; height: 118px;
    background: var(--band-white);
    display: flex; align-items: center; gap: 18px;
    padding-left: 34px;
  }
  .brand-dot {
    width: 76px; height: 76px; border-radius: 50%;
    background: var(--logo-blue);
    flex: none;
  }
  .brand-name {
    font-family: "Open Sans", sans-serif;
    font-weight: 600; font-size: 30px;
    color: var(--logo-blue);
    white-space: nowrap;
  }
</style>
</head>
<body>
  <main class="led-poster">
    <div class="poster-photo" role="img" aria-label="Foto: frierendes Kind mit Mütze und Schal sitzt auf einem kalten Heizkörper vor einer weißen Ziegelwand"></div>

    <section class="headline-block">
      <h1 class="headline-cold">Heizung kalt?</h1>
      <p class="headline-lead">… wir machen's Ihnen</p>
      <p class="headline-warm">Warm ums Herz!</p>
      <p class="phone-number">0 47 11 / 36 20 5-80</p>
    </section>

    <footer class="brand-band">
      <span class="brand-dot"></span>
      <span class="brand-name">Wärmehaus Tellbrink</span>
    </footer>
  </main>
</body>
</html>
```